MOLVT Study flyer

I need help designing a flyer for a research study that will include brain imaging in adolescents. The info is in the attached document. The study is called the Marrowby Orchard Lantern Vesper Trail (MOLVT) study. Ideally this would be returned as a document that I can edit in the future as we will have several new recruitment phases (different age groups, etc. I also would love to have a logo designed as part of this project, but I recognize that might be a separate design request.

```html
<!DOCTYPE html>
<html lang="en">
<head>
<meta charset="utf-8">
<title>MOLVT Study Flyer</title>
<link href="https://fonts.googleapis.com/css2?family=Lexend:wght@300;400;500;600;700;800&display=swap" rel="stylesheet">
<style>
  :root{
    --navy:#0c2a5e;
    --navy-deep:#082152;
    --purple:#5b2f91;
    --purple-soft:#e6dcef;
    --teal:#5fc6c1;
    --teal-dark:#14878a;
    --teal-soft:#cdeeec;
    --blue-soft:#d6e0ef;
    --panel:#eef6f5;
    --ink:#1d1d2b;
    --white:#ffffff;
  }
  *{box-sizing:border-box;margin:0;padding:0}
  html,body{width:953px;height:1200px;overflow:hidden}
  body{
    font-family:"Lexend",sans-serif;
    color:var(--ink);
    background:linear-gradient(180deg,#5a00ff 0%,#2d14b8 45%,#0c2460 80%,#0a2458 100%);
    position:relative;
  }
  .flyer{
    position:absolute;left:92px;top:104px;width:769px;height:993px;
    background:var(--white);overflow:hidden;
  }
  .abs{position:absolute}

  /* header */
  .header-bg{left:0;top:0;width:769px;height:240px;
    background:linear-gradient(90deg,#ffffff 0%,#f2f4f8 40%,#ecebf2 65%,#f3eef6 100%)}
  .hero-photo{left:470px;top:0;width:299px;height:470px;
    background:linear-gradient(160deg,#eae3f1 0%,#c9b2e3 35%,#9d7ad0 70%,#8a66c4 100%)}
  .brand-mark{left:38px;top:48px;width:140px;height:140px;border-radius:50%;background:var(--navy)}
  .brand-name{left:203px;top:58px;font-size:66px;font-weight:700;color:var(--navy);letter-spacing:1px;line-height:1}
  .brand-study{left:203px;top:128px;width:236px;display:flex;align-items:center;gap:10px;
    color:var(--purple);font-size:29px;font-weight:500;letter-spacing:9px}
  .brand-study::before,.brand-study::after{content:"";flex:1;height:2px;background:var(--purple)}
  .brand-study span{margin-right:-9px}
  .brand-full{left:180px;top:172px;width:282px;text-align:center;color:var(--purple);
    font-size:16px;font-weight:400;font-variant:small-caps;line-height:22px}

  .circle-photo{border-radius:50%;border:4px solid var(--white)}
  .circle-chip{left:564px;top:228px;width:212px;height:212px;
    background:radial-gradient(circle at 50% 40%,#7fc2ff 0%,#4a63d6 35%,#5b3aa8 70%,#2b2a77 100%)}
  .circle-mind{left:459px;top:343px;width:140px;height:140px;
    background:radial-gradient(circle at 60% 40%,#d7c6d8 0%,#8a7296 45%,#3d2f4b 100%)}

  /* question band */
  .question-band{left:0;top:239px;width:465px;height:185px;background:var(--navy);color:var(--white)}
  .question{position:absolute;left:50px;top:16px;font-size:29px;font-weight:500;line-height:35px}
  .question .age{color:var(--teal);font-size:40px;font-weight:500}
  .question-rule{position:absolute;left:52px;top:94px;width:280px;height:1px;background:#8a8fbf}
  .dots{position:absolute;left:341px;top:90px;display:flex;gap:10px}
  .dots i{width:8px;height:8px;border-radius:50%;display:block}
  .subquestion{position:absolute;left:50px;top:108px;font-size:28px;font-weight:500;line-height:30px;color:var(--teal)}

  /* intro */
  .intro{left:37px;top:436px;width:420px;border-left:2px solid var(--teal);padding-left:18px;
    font-size:15.5px;font-weight:300;line-height:19.5px}
  .intro strong{color:var(--purple);font-weight:700;font-size:17px}

  /* participation */
  .involves{left:33px;top:553px;width:459px;height:241px;border:1.5px solid var(--purple);border-radius:10px}
  .involves-tag{left:108px;top:540px;width:292px;height:28px;border-radius:14px;background:var(--purple);
    color:var(--white);font-size:15px;font-weight:700;display:flex;align-items:center;justify-content:center;letter-spacing:.2px}
  .step{top:580px;width:150px;text-align:center;font-size:10.5px;font-weight:300;line-height:13.2px}
  .step-icon{width:80px;height:80px;border-radius:50%;margin:0 auto 12px;display:flex;align-items:center;justify-content:center}
  .step h3{font-size:11px;font-weight:700;line-height:13px}
  .divider{width:1.5px;background:#c8bcd8;top:585px;height:195px}

  /* eligibility */
  .eligible{left:512px;top:500px;width:230px;height:295px;background:var(--panel);
    border:3px solid var(--teal-soft);border-radius:12px}
  .eligible-icon{left:589px;top:469px;width:70px;height:70px;border-radius:50%;background:var(--white);
    border:1.5px solid var(--teal);display:flex;align-items:center;justify-content:center}
  .eligible h2{position:absolute;left:21px;top:52px;font-size:16.5px;font-weight:700;color:var(--teal-dark);line-height:21px;letter-spacing:.2px}
  .eligible-rule{position:absolute;left:21px;top:98px;width:190px;height:1.5px;background:var(--teal-dark)}
  .criteria{position:absolute;left:26px;top:112px;list-style:none;width:195px}
  .criteria li{display:flex;gap:8px;font-size:13.5px;font-weight:300;line-height:16.2px;margin-bottom:16px}
  .criteria svg{flex:none;margin-top:1px}

  /* contact & compensation */
  .contact-icon{left:37px;top:826px;width:69px;height:69px;border-radius:50%;border:2px solid var(--purple);
    display:flex;align-items:center;justify-content:center}
  .contact-icon span{width:57px;height:57px;border-radius:50%;background:var(--purple);display:flex;align-items:center;justify-content:center}
  .contact-text{left:123px;top:833px;font-size:16px;font-weight:700;line-height:20.5px}
  .contact-text .l1{color:var(--purple)}
  .contact-text .l2{color:var(--navy)}
  .contact-text em{color:var(--teal-dark);font-weight:400;font-size:16px}
  .contact-rule{left:395px;top:831px;width:1.5px;height:72px;background:#c8c8d6}
  .comp-pill{left:442px;top:820px;width:300px;height:70px;border-radius:35px;background:var(--navy)}
  .comp-icon{left:412px;top:816px;width:79px;height:79px;border-radius:50%;background:var(--white);
    border:2px solid var(--navy);display:flex;align-items:center;justify-content:center}
  .comp-text{left:520px;top:828px;color:var(--white);font-size:18px;font-weight:600;line-height:22px}
  .comp-text .amount{color:var(--teal);font-size:37px;font-weight:600;vertical-align:-4px;margin-left:4px}

  /* footer */
  .footer{left:0;top:912px;width:769px;height:81px;
    background:linear-gradient(90deg,#563089 0%,#2b2f6f 40%,#0f4c7a 70%,#3fb9b8 100%);color:var(--white)}
  .footer-email{position:absolute;left:58px;top:29px;display:flex;align-items:center;gap:7px;font-size:18.5px;font-weight:300}
  .footer-icons{position:absolute;left:482px;top:10px;width:184px;display:flex;justify-content:space-between;align-items:center}
  .footer-icons .sep{width:1px;height:14px;border-left:1px dotted rgba(255,255,255,.6)}
  .footer-note{position:absolute;left:425px;top:41px;width:298px;text-align:center;font-size:10.4px;font-weight:300;line-height:13px}
</style>
</head>
<body>
<main class="flyer">
  <div class="abs header-bg" role="img" aria-label="Soft backdrop of a faint brain with handwritten math formulas"></div>
  <div class="abs hero-photo" role="img" aria-label="Photo of a smiling teenage girl in a purple hoodie, chin resting on her hand, looking upward"></div>

  <div class="abs brand-mark"></div>
  <div class="abs brand-name">MOLVT</div>
  <div class="abs brand-study"><span>STUDY</span></div>
  <div class="abs brand-full">Marrowby Orchard Lantern<br>Vesper Trail</div>

  <section class="abs question-band">
    <p class="question">Are you the parent of a child<br>age <span class="age">10-17</span>?</p>
    <div class="question-rule"></div>
    <div class="dots"><i style="background:#9a7cc7"></i><i style="background:var(--teal)"></i><i style="background:#f2c98a"></i></div>
    <p class="subquestion">Do they worry or overthink<br>negative emotions?</p>
  </section>

  <div class="abs circle-photo circle-chip" role="img" aria-label="Illustration of a glowing blue brain above a circuit board"></div>
  <div class="abs circle-photo circle-mind" role="img" aria-label="Image of a girl in profile with a glowing network over her brain"></div>

  <p class="abs intro">Halvern State University researchers are seeking <strong>girls age 10-17</strong> for a study about brain activity in emotions and decision-making and how they relate to puberty, anxiety and depression.</p>

  <section>
    <div class="abs involves"></div>
    <div class="abs involves-tag">STUDY PARTICIPATION INVOLVES:</div>

    <div class="abs step" style="left:31px">
      <div class="step-icon" style="background:var(--purple-soft)">
        <svg width="46" height="44" viewBox="0 0 46 44" fill="none" stroke="#4a3a86" stroke-width="1.6" stroke-linejoin="round" stroke-linecap="round">
          <rect x="2" y="6" width="14" height="10" rx="2"/><rect x="14" y="1" width="14" height="10" rx="2"/>
          <circle cx="13" cy="24" r="4"/><path d="M5 38c0-6 4-9 8-9s8 3 8 9z"/>
          <circle cx="33" cy="22" r="4.5"/><path d="M24 36c0-6 4-9 9-9s9 3 9 9z"/><path d="M2 40h42"/>
        </svg>
      </div>
      <h3 style="color:var(--purple)">ONE ONE-HOUR<br>INTERVIEW</h3>
      <p>(online or in-person)<br>where your child will<br>discuss their thoughts.</p>
    </div>
    <div class="abs divider" style="left:182px"></div>

    <div class="abs step" style="left:181px">
      <div class="step-icon" style="background:var(--teal-soft)">
        <svg width="50" height="46" viewBox="0 0 50 46" fill="none" stroke="#1f8f92" stroke-width="1.8" stroke-linejoin="round" stroke-linecap="round">
          <rect x="2" y="8" width="40" height="28" rx="2"/><path d="M2 30h40M18 36l-2 6h12l-2-6M12 42h20"/>
          <circle cx="40" cy="9" r="7" fill="#cdeeec"/><path d="M37 9l2.2 2.2L43.5 7"/>
        </svg>
      </div>
      <h3 style="color:var(--teal-dark)">ONLINE<br>QUESTIONNAIRES</h3>
      <p>(parent and child)</p>
    </div>
    <div class="abs divider" style="left:333px"></div>

    <div class="abs step" style="left:332px">
      <div class="step-icon" style="background:var(--blue-soft)">
        <svg width="44" height="46" viewBox="0 0 44 46" fill="none" stroke="#1c4a8a" stroke-width="1.8" stroke-linejoin="round" stroke-linecap="round">
          <rect x="8" y="2" width="22" height="38" rx="3"/><path d="M13 10v16M17 8v20M21 10v16M25 8v14"/>
          <path d="M22 30l6-6 6 4 6 8v8H26z" fill="#1c4a8a"/><path d="M3 14v14M5 18v6"/>
        </svg>
      </div>
      <h3 style="color:#1c4a8a">ONE TWO-HOUR VISIT</h3>
      <p>where your child will<br>complete an MRI scan,<br>answer questions about<br>their puberty stage, and<br>have a small hair sample,<br>taken to study puberty<br>hormones.</p>
    </div>
  </section>

  <section class="abs eligible">
    <h2>YOUR CHILD MAY<br>BE ELIGIBLE IF THEY:</h2>
    <div class="eligible-rule"></div>
    <ul class="criteria">
      <li><svg width="16" height="16" viewBox="0 0 16 16"><circle cx="8" cy="8" r="8" fill="#14878a"/><path d="M4.5 8.2l2.3 2.3L11.5 5.6" fill="none" stroke="#fff" stroke-width="1.8" stroke-linecap="round" stroke-linejoin="round"/></svg><span>Are age 10-17</span></li>
      <li><svg width="16" height="16" viewBox="0 0 16 16"><circle cx="8" cy="8" r="8" fill="#14878a"/><path d="M4.5 8.2l2.3 2.3L11.5 5.6" fill="none" stroke="#fff" stroke-width="1.8" stroke-linecap="round" stroke-linejoin="round"/></svg><span>Tend to worry or overthink negative thoughts</span></li>
      <li><svg width="16" height="16" viewBox="0 0 16 16"><circle cx="8" cy="8" r="8" fill="#14878a"/><path d="M4.5 8.2l2.3 2.3L11.5 5.6" fill="none" stroke="#fff" stroke-width="1.8" stroke-linecap="round" stroke-linejoin="round"/></svg><span>Have not been diagnosed with psychosis, learning problems, or autism</span></li>
    </ul>
  </section>
  <div class="abs eligible-icon">
    <svg width="44" height="42" viewBox="0 0 44 42" fill="none" stroke="#1f6f8a" stroke-width="1.6" stroke-linecap="round" stroke-linejoin="round">
      <circle cx="12" cy="6" r="3.5"/><circle cx="22" cy="5" r="3.5"/><circle cx="32" cy="6" r="3.5"/>
      <path d="M7 22v-8a4 4 0 0 1 8 0v8M17 22v-9a5 5 0 0 1 10 0v9M29 22v-8a4 4 0 0 1 8 0v8"/>
      <path d="M2 28l8-4h10l5 3h-8M2 36l8 1 16-2 14-9-3-2-12 6"/>
    </svg>
  </div>

  <div class="abs contact-icon"><span>
    <svg width="30" height="22" viewBox="0 0 30 22" fill="none" stroke="#fff" stroke-width="1.8" stroke-linejoin="round"><rect x="1" y="1" width="28" height="20"/><path d="M1 1l14 11L29 1M1 21l10-9M29 21l-10-9"/></svg>
  </span></div>
  <div class="abs contact-text">
    <div class="l1">INTERESTED IN PARTICIPATING?</div>
    <div class="l2">WANT MORE INFORMATION?</div>
    <em>Please contact us!</em>
  </div>
  <div class="abs contact-rule"></div>

  <div class="abs comp-pill"></div>
  <div class="abs comp-icon">
    <svg width="46" height="46" viewBox="0 0 46 46" fill="none" stroke="#0c2a5e" stroke-width="1.8" stroke-linejoin="round" stroke-linecap="round">
      <path d="M23 12c-4-7-11-7-11-3s6 3 11 3c5 0 11 1 11-3s-7-4-11 3z"/>
      <rect x="4" y="12" width="38" height="8"/><rect x="7" y="20" width="32" height="22"/><path d="M23 12v30"/>
      <text x="15" y="37" font-family="Lexend,sans-serif" font-size="13" font-weight="600" fill="#0c2a5e" stroke="none" text-anchor="middle">$</text>
      <text x="31" y="37" font-family="Lexend,sans-serif" font-size="13" font-weight="600" fill="#0c2a5e" stroke="none" text-anchor="middle">$</text>
    </svg>
  </div>
  <div class="abs comp-text">COMPENSATION<br>UP TO<span class="amount">$140</span></div>

  <footer class="abs footer">
    <div class="footer-email">
      <svg width="28" height="20" viewBox="0 0 28 20" fill="none" stroke="#fff" stroke-width="1.6" stroke-linejoin="round"><rect x="1" y="1" width="26" height="18"/><path d="M1 1l13 10L27 1M1 19l9-8M27 19l-9-8"/></svg>
      hello@molvtstudy.org
    </div>
    <div class="footer-icons">
      <svg width="26" height="22" viewBox="0 0 26 22" fill="#fff"><circle cx="8" cy="8" r="6"/><circle cx="16" cy="7" r="6.5"/><circle cx="19" cy="13" r="5"/><circle cx="9" cy="14" r="4.5"/><rect x="14" y="15" width="3" height="6" rx="1"/></svg>
      <span class="sep"></span>
      <svg width="24" height="22" viewBox="0 0 24 22" fill="none" stroke="#fff" stroke-width="1.8" stroke-linejoin="round"><path d="M12 20S2 13.5 2 7.2A5 5 0 0 1 12 5a5 5 0 0 1 10 2.2C22 13.5 12 20 12 20z"/></svg>
      <span class="sep"></span>
      <svg width="26" height="24" viewBox="0 0 26 24" fill="#fff"><circle cx="13" cy="6" r="3"/><circle cx="6" cy="10" r="2.5"/><circle cx="20" cy="10" r="2.5"/><path d="M9 21c0-5 2-10 4-10s4 5 4 10zM2 21c0-4 2-7 4-7s3 2 3 4zM24 21c0-4-2-7-4-7s-3 2-3 4z"/></svg>
    </div>
    <p class="footer-note">Your participation helps us understand the developing brain and support adolescent mental health.</p>
  </footer>
</main>
</body>
</html>
```